Womans Supplement Designs

Launching a Supplement company and need to get some initial designs created, I've attached our logo and the bottle type that I want the samples done one.

This project is for our Whey Protein we are starting with Vanilla, chocolate and strawberry banana

(ALL DESIGN VARIATIONS MUST BE A WHITE BOTTLE NOT BLACK)

(FOR DESIGN SAMPLES PLEASE USE THE SUPPLEMENT BOTTLE STYLE I PROVIDED)

Whoever is selected the winner I will have more work for you to complete the disigns for the rest of the products in the line, Just want to get this shake completed first

Target Market(s)

Women

Requirements
Must have
• Must have our current logo involved

the name of this product will be "KIVA LUM"

Must have this slogan,

ALL-IN-ONE PREMIUM PROTEIN NUTRITIONAL SHAKE FOR BLACK WOMEN

This is our meal replacement

the design should try to keep the same look and feel of the existing provided supplement images

we are starting with chocolate, vanilla and strawberry banana

this is for women and should look colorful and appeal to them
Should not have
• Do not use an image of a person or lady, don't want it branded to a person

```html
<!DOCTYPE html>
<html lang="en">
<head>
<meta charset="UTF-8">
<title>KIVA LUM – Chocolate Protein Shake</title>
<link rel="stylesheet" href="https://fonts.googleapis.com/css2?family=Poppins:wght@200;500&family=Oswald:wght@500;600&display=swap">
<style>
  :root {
    --canvas: #ffffff;
    --ink: #111111;
    --ink-soft: #3a3a3a;
    --brand-box: #0d0d0d;
    --brand-text: #ffffff;
    --badge-line: #222222;
    --bottle-light: #ffffff;
    --bottle-edge: #e4e6ea;
    --bottle-blush: #fbeef2;
    --cap-light: #fafafa;
    --cap-shade: #dcdde0;
    --accent-rose: #c2456e;
    --cocoa-dark: #3b2217;
    --cocoa-mid: #7a4a31;
    --milk: #f3efe8;
  }
  * { margin: 0; padding: 0; box-sizing: border-box; }
  html, body {
    width: 1200px;
    height: 849px;
    overflow: hidden;
    background: var(--canvas);
  }
  .label {
    position: relative;
    width: 1200px;
    height: 849px;
    font-family: "Poppins", sans-serif;
    color: var(--ink);
  }
  .bottle {
    position: absolute;
    left: 0;
    top: 0;
    width: 1200px;
    height: 849px;
  }
  .brand-box {
    position: absolute;
    left: 547px;
    top: 162px;
    width: 153px;
    height: 111px;
    background: var(--brand-box);
    display: flex;
    align-items: center;
    justify-content: center;
    text-align: center;
  }
  .brand-name {
    color: var(--brand-text);
    font-weight: 500;
    font-size: 13px;
    letter-spacing: 2.5px;
    line-height: 1.5;
  }
  .product-name {
    position: absolute;
    left: 388px;
    top: 312px;
    width: 460px;
    text-align: center;
    font-weight: 200;
    font-size: 70px;
    letter-spacing: 4px;
    line-height: 1;
  }
  .slogan {
    position: absolute;
    left: 398px;
    top: 392px;
    width: 440px;
    text-align: center;
    font-weight: 500;
    font-size: 9.5px;
    letter-spacing: 1.2px;
    line-height: 1.3;
    color: var(--accent-rose);
  }
  .flavour-visual {
    position: absolute;
    left: 466px;
    top: 424px;
    width: 270px;
    height: 240px;
    border-radius: 46% 42% 30% 38%;
    background:
      radial-gradient(ellipse 38% 34% at 40% 62%, var(--cocoa-mid) 0%, var(--cocoa-dark) 70%, rgba(59,34,23,0) 100%),
      radial-gradient(ellipse 14% 10% at 62% 18%, var(--cocoa-mid) 0%, var(--cocoa-dark) 80%, rgba(59,34,23,0) 100%),
      radial-gradient(ellipse 50% 48% at 55% 55%, var(--milk) 0%, var(--milk) 60%, rgba(243,239,232,0) 100%);
  }
  .spec-badge {
    position: absolute;
    left: 759px;
    top: 450px;
    width: 52px;
    height: 172px;
    border: 1.5px solid var(--badge-line);
    border-radius: 26px;
    display: flex;
    flex-direction: column;
    justify-content: space-evenly;
    align-items: center;
    text-align: center;
  }
  .spec-value {
    font-family: "Oswald", sans-serif;
    font-weight: 600;
    font-size: 19px;
    line-height: 1;
    color: var(--ink-soft);
  }
  .spec-unit {
    display: block;
    font-family: "Oswald", sans-serif;
    font-weight: 500;
    font-size: 5px;
    letter-spacing: 0.3px;
    line-height: 1.3;
    margin-top: 2px;
  }
  .flavour-band {
    position: absolute;
    left: 495px;
    top: 664px;
    width: 254px;
    height: 40px;
    border-radius: 20px;
    background: var(--brand-box);
    color: var(--brand-text);
    font-family: "Oswald", sans-serif;
    font-weight: 600;
    font-size: 19px;
    letter-spacing: 0.5px;
    display: flex;
    align-items: center;
    justify-content: center;
  }
</style>
</head>
<body>
  <main class="label">
    <svg class="bottle" viewBox="0 0 1200 849" aria-hidden="true">
      <defs>
        <linearGradient id="bottle-body" x1="0" y1="0" x2="1" y2="0">
          <stop offset="0" stop-color="var(--bottle-edge)"/>
          <stop offset="0.18" stop-color="var(--bottle-light)"/>
          <stop offset="0.8" stop-color="var(--bottle-light)"/>
          <stop offset="1" stop-color="var(--bottle-edge)"/>
        </linearGradient>
        <linearGradient id="bottle-blush" x1="0" y1="0" x2="0" y2="1">
          <stop offset="0.55" stop-color="var(--bottle-blush)" stop-opacity="0"/>
          <stop offset="1" stop-color="var(--bottle-blush)" stop-opacity="1"/>
        </linearGradient>
        <linearGradient id="bottle-cap" x1="0" y1="0" x2="0" y2="1">
          <stop offset="0" stop-color="var(--cap-light)"/>
          <stop offset="1" stop-color="var(--cap-shade)"/>
        </linearGradient>
      </defs>
      <rect x="430" y="150" width="376" height="22" rx="4" fill="var(--cap-shade)"/>
      <path d="M440 168 H796 Q848 180 848 262 V735 Q848 763 820 763 H416 Q388 763 388 735 V262 Q388 180 440 168 Z" fill="url(#bottle-body)"/>
      <path d="M440 168 H796 Q848 180 848 262 V735 Q848 763 820 763 H416 Q388 763 388 735 V262 Q388 180 440 168 Z" fill="url(#bottle-blush)"/>
      <rect x="424" y="96" width="388" height="60" rx="8" fill="url(#bottle-cap)"/>
    </svg>

    <div class="brand-box">
      <span class="brand-name">NOVA BLOOM<br>WELLNESS</span>
    </div>

    <h1 class="product-name">KIVA LUM</h1>

    <p class="slogan">ALL-IN-ONE PREMIUM PROTEIN NUTRITIONAL SHAKE FOR BLACK WOMEN</p>

    <div class="flavour-visual" role="img" aria-label="Chocolate bar pieces and shavings with a splash of milk"></div>

    <div class="spec-badge">
      <div class="spec-value">50<span class="spec-unit">CAPSULES</span></div>
      <div class="spec-value">27<span class="spec-unit">PROTEIN<br>GRAMS</span></div>
      <div class="spec-value">500<span class="spec-unit">GRAMS</span></div>
    </div>

    <div class="flavour-band">CHOCOLATE</div>
  </main>
</body>
</html>
```